Non profit housing agency needs a brochure design

We need a brochure design for our non profit housing organization, 'TAVOL, Inc.' The message we would like to communicate is: "We Have A Place You Can Call Home". Our agency provides housing for the homeless and at-risk. In the brochure, we want to tell the public about our 3 agency programs.
1. The BRIDGE (Builders Reaching Into Daily Growth) Program- for homeless adult men ex-offenders
2. Marla's Garden- for homeless adult women ex-offenders and their children
3. Delphine's Harbor- for domestic minor victims of sex trafficking
TAVOL, Inc. is a housing organization that serves various populations in the above programs. Attached is our newly designed logo from a talented Artmingle designer. We would like to build on this design using the same colors and creativity.
Target Market(s)
Government, churches, public
Industry/Entity Type
Non Profit
Look and feel

```html
<!DOCTYPE html>
<html lang="en">
<head>
<meta charset="utf-8">
<title>TAVOL, Inc. — We Have A Place You Can Call Home</title>
<link rel="stylesheet" href="https://fonts.googleapis.com/css2?family=Cinzel:wght@400;500&family=Lato:wght@400;700&display=swap">
<style>
  :root {
    --sky-top: #173f9e;
    --sky-mid: #3f7ad0;
    --sky-low: #a9c8ee;
    --grass-top: #7cc234;
    --grass-low: #3f8a16;
    --panel: rgba(255, 255, 255, 0.92);
    --accent: #e8641e;
    --ink: #1e1e1e;
    --headline: #ffffff;
    --headline-accent: #f6e21a;
    --footer-bg: #1d2a6e;
    --footer-text: #ffffff;
    --footer-accent: #f6e21a;
  }
  * { box-sizing: border-box; margin: 0; padding: 0; }
  html, body { width: 926px; height: 1200px; overflow: hidden; background: #ffffff; }
  .brochure {
    position: relative;
    width: 926px;
    height: 1200px;
    overflow: hidden;
    font-family: "Lato", sans-serif;
    color: var(--ink);
  }
  .scene {
    position: absolute;
    inset: 0;
    background: linear-gradient(180deg,
      var(--sky-top) 0%,
      var(--sky-mid) 35%,
      var(--sky-low) 62%,
      var(--grass-top) 70%,
      var(--grass-low) 100%);
  }
  .info-panel {
    position: absolute;
    left: 55px;
    top: 0;
    width: 327px;
    height: 1144px;
    background: linear-gradient(180deg, var(--panel) 0%, var(--panel) 72%, rgba(255,255,255,0.55) 90%, rgba(255,255,255,0) 100%);
  }
  .brand-name {
    position: absolute; left: 96px; top: 98px;
    font-family: "Lato", sans-serif;
    font-size: 44px; font-weight: 400; line-height: 1;
    color: var(--accent);
  }
  .panel-copy {
    position: absolute; left: 80px; width: 282px;
    font-size: 13.5px; line-height: 20px;
  }
  .intro { top: 216px; }
  .programs { top: 292px; list-style: none; }
  .program { display: flex; gap: 12px; margin-bottom: 18px; }
  .program-num, .program-title { color: var(--accent); }
  .program-num { width: 8px; flex: none; }
  .about { top: 560px; }
  .about p { margin-bottom: 20px; text-align: justify; }
  .about p:first-child { text-align: left; }
  .headline {
    position: absolute; left: 436px; top: 176px;
    font-family: "Cinzel", serif; font-weight: 400;
    color: var(--headline); font-size: 60px; line-height: 63px;
    text-shadow: 0 2px 6px rgba(0,0,0,0.35);
  }
  .headline-accent {
    display: block; color: var(--headline-accent);
    font-size: 104px; line-height: 96px; margin-top: 4px;
  }
  .contact-bar {
    position: absolute; left: 0; bottom: 0; width: 926px; height: 56px;
    background: var(--footer-bg); color: var(--footer-text);
    display: flex; align-items: center; gap: 20px; padding-left: 46px;
    font-size: 14px;
  }
  .contact-web { margin-left: auto; margin-right: 40px; color: var(--footer-accent); font-weight: 700; font-size: 16px; }
</style>
</head>
<body>
<div class="brochure">
  <div class="scene" role="img" aria-label="Photo of a red-roofed brick house on a green meadow under a blue sky with white clouds"></div>

  <div class="info-panel"></div>

  <div class="brand-name">TAVOL, Inc.</div>

  <p class="panel-copy intro">Our agency provides housing for the homeless and at-risk. They are :-</p>

  <ol class="panel-copy programs">
    <li class="program"><span class="program-num">1</span><span><span class="program-title">The BRIDGE<br>(Builders Reaching Into Daily Growth) Program -</span><br>for homeless adult men ex-offenders</span></li>
    <li class="program"><span class="program-num">2</span><span><span class="program-title">Marla's Garden -</span><br>for homeless adult women<br>ex-offenders and their children</span></li>
    <li class="program"><span class="program-num">3</span><span><span class="program-title">Delphine's Harbor -</span><br>for domestic minor victims of<br>sex trafficking</span></li>
  </ol>

  <div class="panel-copy about">
    <p>We need a brochure design for our non profit housing organization, 'TAVOL, Inc.' The message we would like to communicate is: "We Have A Place You Can Call Home".</p>
    <p>Our agency provides housing for the homeless and at-risk. In the brochure, we want to tell the public about our 3 agency programs We need a brochure design for our non profit housing organization, 'TAVOL, Inc.' The message we would like to communicate is: "We Have A Place You Can Call Home". Our agency provides housing for the homeless and at-risk. In the brochure, we want to tell the public about our 3 agency programs</p>
  </div>

  <h1 class="headline">WE HAVE<br>A PLACE YOU<br>CAN CALL<span class="headline-accent">HOME</span></h1>

  <footer class="contact-bar">
    <span>412 Maplecrest Rd. Dayton, OH 45402</span>
    <span>Phone: 555-204-7731</span>
    <span>Email: info@tavolinc.org</span>
    <span class="contact-web">www.tavolinc.org</span>
  </footer>
</div>
</body>
</html>
```